Brightrankkit.com Website Design

We would like to redesign brightrnkkit.com and we are looking for creative ideas. The new design should be clean and not resemble with any other existing website design.

The most important factor is that website have many banners/advertisements so the new design should be able to accommodate these banners of different size (Advertisement Friendly Design)

All Tools should be categorized under different main categories like all those tools that are related to content/writing will be shown under Content Tools ( Please find all categories and tools in attached file with the project). Right now all tools are showing randomly.

Also, Design single tool pages with sidebar, advertisement, and content placement.
ex. brightrankkit.com/plagiarism-checker/
brightrankkit.com/keyword-position/

Winning designer will also make the logo as well.

Target Market(s)

SEO Agencies, SEO executive, Article writers, Essay Writers, Plagiarism Checkers, Webmasters

Industry/Entity Type

Seo

Logo Text

Bright Rank Kit

Number of Pages Required

5+ page

Font styles to use
Serif
Sans Serif
Other font styles liked:
• Any

Colors

Designer to choose colors to be used in the design.

Requirements
Must have
• 1) Clean Design
• 2) Modern Look
• 3) Easy To Navigate
• 4) Separate Icon for every Tool
• 5) Advertisement/Banners Freindly Design
Nice to have
• Matching Logo
• WOW Factor
Should not have
• Complex Design
• No drop down menu

```html
<!DOCTYPE html>
<html lang="en">
<head>
<meta charset="utf-8">
<title>Bright Rank Kit – SEO Tools</title>
<link href="https://fonts.googleapis.com/css2?family=Poppins:wght@400;500;600;700&display=swap" rel="stylesheet">
<style>
:root{
  --blue:#1e88e5;
  --blue-dark:#1565c0;
  --icon:#1976d2;
  --ink:#2b2f36;
  --muted:#6b7280;
  --line:#e3e6ea;
  --grey-band:#f3f4f6;
  --orange:#f7892a;
  --green:#22c35e;
  --green-dark:#1b7a45;
  --footer:#3b4553;
  --footer-deep:#2e3743;
  --white:#ffffff;
}
*{box-sizing:border-box;margin:0;padding:0}
html,body{width:1200px;height:5000px;overflow:hidden}
body{font-family:"Poppins",sans-serif;color:var(--ink);background:var(--white)}
.wrap{width:1026px;margin:0 auto}

/* header */
.site-header{height:73px;background:var(--white);display:flex;align-items:center;justify-content:space-between;padding:0 87px;border-bottom:1px solid var(--line)}
.brand{display:flex;align-items:center;gap:10px}
.brand-mark{width:26px;height:26px;background:var(--blue-dark)}
.brand-text{display:flex;flex-direction:column;line-height:1}
.brand-name{font-size:22px;font-weight:700;color:var(--blue-dark)}
.brand-tag{font-size:10px;color:var(--muted);margin-top:3px;letter-spacing:.5px}
.main-nav{display:flex;align-items:center;gap:26px;font-size:13px}
.main-nav a{color:var(--ink);text-decoration:none;white-space:nowrap}
.main-nav .active{background:#e8f2fc;color:var(--blue);padding:6px 14px;border-radius:3px}
.main-nav .login{color:var(--green);font-weight:500}
.main-nav .register{background:var(--green);color:var(--white);padding:8px 22px;border-radius:20px;font-weight:500}

/* hero */
.hero{height:234px;background:linear-gradient(135deg,#1e88e5,#2196f3 60%,#1976d2);display:flex;flex-direction:column;align-items:center;padding-top:68px}
.hero h1{color:var(--white);font-size:26px;font-weight:500}
.search-box{margin-top:22px;width:440px;height:48px;background:var(--white);border-radius:24px;display:flex;align-items:center;padding:0 22px;gap:12px;color:#a0a6ad;font-size:13px}

/* tabs */
.category-tabs{height:43px;border-bottom:1px solid var(--line);display:flex;align-items:center;justify-content:space-between;padding:0 90px;font-size:11.5px;color:var(--muted)}
.category-tabs span{white-space:nowrap;line-height:43px;height:43px}
.category-tabs .current{color:var(--ink);border-bottom:2px solid var(--blue)}

/* sections */
.tool-section{padding-top:68px}
.tool-section h2{text-align:center;font-size:26px;font-weight:500;line-height:36px;margin-bottom:23px}
.tool-section.grey{background:var(--grey-band)}
.tool-section.orange{background:var(--orange)}
.tool-section.orange h2{color:var(--white)}
.s-content{height:733px}.s-images{height:567px}.s-keywords{height:717px}.s-backlinks{height:523px}.s-website{height:1677px}

.tool-grid{display:grid;grid-template-columns:repeat(4,240px);gap:21px 22px}
.tool-card{height:166px;background:var(--white);border:1px solid var(--line);display:flex;flex-direction:column;align-items:center;justify-content:center;gap:20px;font-size:14px;text-align:center;padding:0 14px}
.tool-card svg{width:56px;height:56px;fill:none;stroke:var(--icon);stroke-width:2.2;stroke-linecap:round;stroke-linejoin:round}
.tool-card.load-more{background:#e6f1fb;border-color:#d4e6f7;color:var(--blue-dark)}

.ad-plagiarism{height:166px;background:linear-gradient(135deg,#1f8f52,var(--green-dark));color:var(--white);padding:18px 20px;display:flex;flex-direction:column;justify-content:center;position:relative}
.ad-plagiarism .try{position:absolute;top:14px;right:16px;font-size:11px}
.ad-plagiarism strong{font-size:25px;line-height:1.15;font-weight:700}
.ad-plagiarism span{font-size:12px;margin-top:6px}
.ad-backlinks{height:166px;background:linear-gradient(120deg,#7a1d1d,#c0392b 55%,#e0522f);color:var(--white);display:flex;flex-direction:column;justify-content:center;align-items:flex-end;padding-right:20px}
.ad-backlinks strong{font-size:34px;font-weight:700;line-height:1}
.ad-backlinks b{font-size:26px;font-weight:700}
.ad-backlinks em{font-style:normal;background:#f5c518;color:#222;font-weight:600;font-size:14px;padding:3px 10px;margin-top:6px}

/* newsletter */
.newsletter{height:100px;background:var(--green);display:flex;align-items:center;justify-content:space-between;padding:0 87px}
.newsletter h3{color:var(--white);font-size:22px;font-weight:600}
.subscribe{display:flex;gap:10px}
.subscribe .field{width:280px;height:40px;border-radius:20px;background:var(--white);font-size:12px;color:#9aa1a8;display:flex;align-items:center;padding:0 20px}
.subscribe .btn{height:40px;padding:0 26px;border:1.5px solid var(--white);border-radius:20px;color:var(--white);font-size:13px;display:flex;align-items:center}

/* footer */
.site-footer{height:293px;background:var(--footer);color:#c8cdd4;display:flex;flex-direction:column;align-items:center;padding-top:62px;font-size:13px}
.site-footer .brand-name{color:var(--white)}
.site-footer .brand-mark{background:var(--white)}
.site-footer .brand-tag{color:#c8cdd4}
.footer-about{margin-top:22px;max-width:760px;text-align:center}
.footer-links{margin-top:18px;display:flex;gap:22px}
.copyright{height:40px;background:var(--footer-deep);color:#c8cdd4;font-size:12px;display:flex;align-items:center;justify-content:center}
</style>
</head>
<body>

<svg width="0" height="0" style="position:absolute" aria-hidden="true">
  <defs>
    <symbol id="i-doc" viewBox="0 0 56 56"><path d="M14 6h20l10 10v34H14z"/><path d="M34 6v10h10M20 26h16M20 33h16M20 40h10"/></symbol>
    <symbol id="i-pen" viewBox="0 0 56 56"><rect x="10" y="10" width="30" height="38"/><path d="M44 14 28 34l-4 6 6-4L46 16z"/></symbol>
    <symbol id="i-text" viewBox="0 0 56 56"><path d="M14 12h28M28 12v34M22 46h12"/></symbol>
    <symbol id="i-spell" viewBox="0 0 56 56"><path d="M8 40 16 16l8 24M11 32h10M30 16h8a5 5 0 0 1 0 10h-8zM30 26h9a6 6 0 0 1 0 14h-9z"/><path d="M40 12l4 4 8-8"/></symbol>
    <symbol id="i-grid" viewBox="0 0 56 56"><rect x="8" y="8" width="16" height="16"/><rect x="32" y="8" width="16" height="16"/><rect x="8" y="32" width="16" height="16"/><path d="M32 32h6v6h-6zM42 42h6v6h-6zM32 44h4M44 32v6"/></symbol>
    <symbol id="i-image" viewBox="0 0 56 56"><rect x="8" y="12" width="40" height="32"/><path d="m8 38 12-12 10 10 6-6 12 12"/><circle cx="36" cy="22" r="3"/></symbol>
    <symbol id="i-compress" viewBox="0 0 56 56"><circle cx="28" cy="28" r="20"/><path d="M18 18l8 8M38 38l-8-8M26 18v8h-8M30 38v-8h8"/></symbol>
    <symbol id="i-crop" viewBox="0 0 56 56"><path d="M16 6v34h34M6 16h34v34"/></symbol>
    <symbol id="i-chart" viewBox="0 0 56 56"><path d="M8 48h40M14 40v-8M24 40V26M34 40V18M44 40V10"/></symbol>
    <symbol id="i-search" viewBox="0 0 56 56"><rect x="8" y="8" width="30" height="38"/><circle cx="34" cy="34" r="9"/><path d="m41 41 8 8M14 16h18M14 22h12"/></symbol>
    <symbol id="i-link" viewBox="0 0 56 56"><path d="M24 32a8 8 0 0 0 11 0l8-8a8 8 0 0 0-11-11l-4 4"/><path d="M32 24a8 8 0 0 0-11 0l-8 8a8 8 0 0 0 11 11l4-4"/></symbol>
    <symbol id="i-list" viewBox="0 0 56 56"><path d="M20 14h28M20 28h28M20 42h28"/><circle cx="10" cy="14" r="2"/><circle cx="10" cy="28" r="2"/><circle cx="10" cy="42" r="2"/></symbol>
    <symbol id="i-globe" viewBox="0 0 56 56"><circle cx="28" cy="28" r="20"/><path d="M8 28h40M28 8c-8 10-8 30 0 40M28 8c8 10 8 30 0 40"/></symbol>
    <symbol id="i-gauge" viewBox="0 0 56 56"><path d="M8 40a20 20 0 1 1 40 0"/><path d="m28 40 10-14"/><circle cx="28" cy="40" r="3"/></symbol>
    <symbol id="i-code" viewBox="0 0 56 56"><rect x="6" y="10" width="44" height="36"/><path d="M6 18h44M22 26l-6 6 6 6M34 26l6 6-6 6"/></symbol>
    <symbol id="i-mail" viewBox="0 0 56 56"><rect x="6" y="14" width="44" height="30"/><path d="m6 14 22 18 22-18"/></symbol>
    <symbol id="i-phone" viewBox="0 0 56 56"><rect x="16" y="6" width="24" height="44" rx="3"/><path d="M24 42h8"/></symbol>
    <symbol id="i-play" viewBox="0 0 56 56"><rect x="6" y="12" width="44" height="32" rx="6"/><path d="m24 21 11 7-11 7z"/></symbol>
    <symbol id="i-camera" viewBox="0 0 56 56"><rect x="8" y="8" width="40" height="40"/><circle cx="28" cy="30" r="9"/><path d="M20 16h6"/></symbol>
    <symbol id="i-signal" viewBox="0 0 56 56"><circle cx="28" cy="28" r="4"/><path d="M18 18a14 14 0 0 0 0 20M38 18a14 14 0 0 1 0 20M12 12a22 22 0 0 0 0 32M44 12a22 22 0 0 1 0 32"/></symbol>
    <symbol id="i-monitor" viewBox="0 0 56 56"><rect x="6" y="10" width="44" height="28"/><path d="M22 46h12M28 38v8"/></symbol>
    <symbol id="i-calc" viewBox="0 0 56 56"><rect x="12" y="6" width="32" height="44"/><path d="M18 12h20v8H18zM20 28h2M28 28h2M36 28h2M20 36h2M28 36h2M36 36h2"/></symbol>
    <symbol id="i-shield" viewBox="0 0 56 56"><path d="M28 6 46 12v14c0 12-8 20-18 24-10-4-18-12-18-24V12z"/><path d="m20 28 6 6 12-12"/></symbol>
    <symbol id="i-plus" viewBox="0 0 56 56"><path d="M28 8v40M8 28h40"/></symbol>
  </defs>
</svg>

<header class="site-header">
  <div class="brand">
    <span class="brand-mark"></span>
    <div class="brand-text"><span class="brand-name">Bright Rank Kit</span><span class="brand-tag">Free Online SEO Tools</span></div>
  </div>
  <nav class="main-nav">
    <a class="active">Home</a><a>Plagiarism Checker</a><a>Advertise</a><a>Blog</a><a>Contact Us</a>
    <a class="login">Login</a><a class="register">Register</a>
  </nav>
</header>

<section class="hero">
  <h1>SEO Tools</h1>
  <div class="search-box">
    <svg width="16" height="16" viewBox="0 0 16 16" fill="none" stroke="#a0a6ad" stroke-width="2"><circle cx="7" cy="7" r="5"/><path d="m11 11 4 4"/></svg>
    Type here to search from 300 tools
  </div>
</section>

<nav class="category-tabs">
  <span class="current">Content Tools</span><span>Images Handling Tool</span><span>Keywords Tools</span><span>Backlink Tools</span><span>Website Tools</span><span>Tracking Tools</span><span>Proxy Tools</span><span>Domain Tools</span><span>Meta Tools</span><span>Password Tools</span><span>PDF Tools</span>
</nav>

<section class="tool-section s-content">
  <h2>Content Tools</h2>
  <div class="wrap tool-grid">
    <div class="tool-card"><svg><use href="#i-doc"/></svg>Plagiarism Checker</div>
    <div class="tool-card"><svg><use href="#i-pen"/></svg>Article Rewriter</div>
    <div class="tool-card"><svg><use href="#i-search"/></svg>Grammar Checker</div>
    <div class="tool-card"><svg><use href="#i-doc"/></svg>Word Count Checker</div>
    <div class="tool-card"><svg><use href="#i-spell"/></svg>Spell Checker</div>
    <div class="tool-card"><svg><use href="#i-grid"/></svg>Online MD5 Generator</div>
    <div class="tool-card"><svg><use href="#i-spell"/></svg>Change Text Case</div>
    <div class="tool-card"><svg><use href="#i-text"/></svg>Merge Words Online Tool</div>
    <div class="tool-card"><svg><use href="#i-image"/></svg>Image to text</div>
  </div>
</section>

<section class="tool-section grey s-images">
  <h2>Images Handling Tool</h2>
  <div class="wrap tool-grid">
    <div class="tool-card"><svg><use href="#i-search"/></svg>Reverse Image Search</div>
    <div class="tool-card"><svg><use href="#i-compress"/></svg>Image Compression</div>
    <div class="tool-card"><svg><use href="#i-image"/></svg>Favicon Generator</div>
    <div class="tool-card"><svg><use href="#i-play"/></svg>Video to gif Converter</div>
    <div class="tool-card"><svg><use href="#i-crop"/></svg>Image Resizer</div>
    <div class="tool-card"><svg><use href="#i-crop"/></svg>Crop Image</div>
    <div class="tool-card"><svg><use href="#i-image"/></svg>Convert to JPG</div>
    <div class="ad-plagiarism"><span class="try">Try now Free</span><strong>Premium Plagiarism Checker</strong><span>with Unlimited Searches</span></div>
  </div>
</section>

<section class="tool-section s-keywords">
  <h2>Keywords Tools</h2>
  <div class="wrap tool-grid">
    <div class="tool-card"><svg><use href="#i-chart"/></svg>Keyword Position</div>
    <div class="tool-card"><svg><use href="#i-search"/></svg>Keywords Density Checker</div>
    <div class="tool-card"><svg><use href="#i-list"/></svg>Keywords Suggestions Tool</div>
    <div class="tool-card"><svg><use href="#i-code"/></svg>Website Keyword Suggestions Tool</div>
    <div class="tool-card"><svg><use href="#i-pen"/></svg>Keywords Rich Domains Suggestions Tool</div>
    <div class="tool-card"><svg><use href="#i-globe"/></svg>Related Keywords Finder</div>
    <div class="tool-card"><svg><use href="#i-gauge"/></svg>Long Tail Keyword Suggestion</div>
    <div class="tool-card"><svg><use href="#i-calc"/></svg>Keyword Competition Checker</div>
    <div class="tool-card"><svg><use href="#i-chart"/></svg>SEO Keyword Competition Analysis</div>
  </div>
</section>

<section class="tool-section orange s-backlinks">
  <h2>BackLink Tools</h2>
  <div class="wrap tool-grid">
    <div class="tool-card"><svg><use href="#i-link"/></svg>Backlink Checker</div>
    <div class="tool-card"><svg><use href="#i-link"/></svg>Backlink Maker</div>
    <div class="tool-card"><svg><use href="#i-list"/></svg>Website Link Count Checker</div>
    <div class="tool-card"><svg><use href="#i-code"/></svg>Website Broken Link Checker</div>
    <div class="ad-backlinks" role="img" aria-label="Backlinks advertisement banner with a bird photograph on a red background"><strong>DA70+</strong><b>Backlinks</b><em>$5/Month</em></div>
    <div class="tool-card"><svg><use href="#i-calc"/></svg>Link Price Calculator</div>
    <div class="tool-card"><svg><use href="#i-link"/></svg>Reciprocal Link Checker</div>
    <div class="tool-card"><svg><use href="#i-globe"/></svg>Website Link Analyzer Tool</div>
  </div>
</section>

<section class="tool-section s-website">
  <h2>Website Tools</h2>
  <div class="wrap tool-grid">
    <div class="tool-card"><svg><use href="#i-grid"/></svg>Website SEO Score Checker</div>
    <div class="tool-card"><svg><use href="#i-chart"/></svg>Rankly PageScore Checker</div>
    <div class="tool-card"><svg><use href="#i-signal"/></svg>Online Ping Website Tool</div>
    <div class="tool-card"><svg><use href="#i-gauge"/></svg>Website Page Speed Checker</div>
    <div class="tool-card"><svg><use href="#i-compress"/></svg>Website Page Size Checker</div>
    <div class="tool-card"><svg><use href="#i-code"/></svg>Website Page Snooper</div>
    <div class="tool-card"><svg><use href="#i-calc"/></svg>Website Hit Counter</div>
    <div class="tool-card"><svg><use href="#i-list"/></svg>XML Sitemap Generator</div>
    <div class="tool-card"><svg><use href="#i-link"/></svg>URL Rewriting Tool</div>
    <div class="tool-card"><svg><use href="#i-monitor"/></svg>Screen Resolution Simulator</div>
    <div class="tool-card"><svg><use href="#i-calc"/></svg>AdYield Calculator</div>
    <div class="tool-card"><svg><use href="#i-doc"/></svg>Open Graph Generator</div>
    <div class="tool-card"><svg><use href="#i-grid"/></svg>QR Code Generator</div>
    <div class="tool-card"><svg><use href="#i-doc"/></svg>Htaccess redirect Generator</div>
    <div class="tool-card"><svg><use href="#i-code"/></svg>Get HTTP Header</div>
    <div class="tool-card"><svg><use href="#i-list"/></svg>Chirper Card Generator</div>
    <div class="tool-card"><svg><use href="#i-gauge"/></svg>NetLine Speed Test</div>
    <div class="tool-card"><svg><use href="#i-search"/></svg>PressKit Theme Detector</div>
    <div class="tool-card"><svg><use href="#i-search"/></svg>Instant Search Suggestion</div>
    <div class="tool-card"><svg><use href="#i-shield"/></svg>Avera Antivirus Checker</div>
    <div class="tool-card"><svg><use href="#i-camera"/></svg>Website Screenshot Generator</div>
    <div class="tool-card"><svg><use href="#i-mail"/></svg>Email Privacy</div>
    <div class="tool-card"><svg><use href="#i-phone"/></svg>Mobile Friendly Test</div>
    <div class="tool-card"><svg><use href="#i-play"/></svg>Vidstream Video Downloader</div>
    <div class="tool-card"><svg><use href="#i-doc"/></svg>CSS Minifier</div>
    <div class="tool-card"><svg><use href="#i-code"/></svg>HTML Minifier</div>
    <div class="tool-card"><svg><use href="#i-doc"/></svg>JS Minifier</div>
    <div class="tool-card"><svg><use href="#i-doc"/></svg>Robots.txt Generator</div>
    <div class="tool-card load-more"><svg><use href="#i-plus"/></svg>Load More Tools</div>
  </div>
</section>

<section class="newsletter">
  <h3>Subscribe for Newsletters:</h3>
  <div class="subscribe"><span class="field">Enter your email address</span><span class="btn">Subscribe</span></div>
</section>

<footer class="site-footer">
  <div class="brand">
    <span class="brand-mark"></span>
    <div class="brand-text"><span class="brand-name">Bright Rank Kit</span><span class="brand-tag">Free Online SEO Tools</span></div>
  </div>
  <p class="footer-about">Bright Rank Kit is one of the biggest free SEO tools provider. All tools are on premium quality and totally free.</p>
  <div class="footer-links"><span>Terms of Services</span><span>Testimonials</span><span>Privacy</span><span>Contact Us</span></div>
</footer>
<div class="copyright">Copyright © 2012-2017 by BrightRankKit.com. All Rights Reserved.</div>

</body>
</html>
```